Q & Q Fabrications HVAC Mechanical Contractor Business Card

We need a business card for a HVAC/Plumbing Mechanical Contractor. Our website is http://www.qqfabrications-example.com. We would like to include the picture of the person on the card. Pictures of people for mock-ups can be found on our website. The blue on our logo is our primary color. We'd like this to be bold yet professional without too many colors but with some color to make sure it stands out.

Industry/Entity Type

Business

Contact Information for Business Card

Font styles to use
Sans Serif

Colors
000000

Requirements
Must have
• Our logo
• Person's picture
• Company Name
• Company Phone
• Person's email address
• Person's phone number
Nice to have
• Company Address
Should not have
• Clip art

```html
<!DOCTYPE html>
<html lang="en">
<head>
<meta charset="utf-8">
<title>Q &amp; Q Fabrications – Business Card</title>
<link href="https://fonts.googleapis.com/css2?family=Source+Sans+3:wght@400;600;800&family=Questrial&display=swap" rel="stylesheet">
<style>
  :root {
    --brand-blue: #3a70c0;
    --brand-blue-deep: #2456a8;
    --ink: #111111;
    --paper: #ffffff;
    --backdrop: #2a2c30;
    --photo-top: #5b5f63;
    --photo-bottom: #2b2e31;
  }
  * { box-sizing: border-box; margin: 0; padding: 0; }
  html, body {
    width: 1200px; height: 790px; overflow: hidden;
    background: var(--backdrop);
  }
  .card {
    position: absolute; left: 75px; top: 95px;
    width: 1050px; height: 600px;
    background: var(--paper);
    font-family: "Source Sans 3", sans-serif;
    color: var(--ink);
    overflow: hidden;
  }
  .brand-mark {
    position: absolute; left: 50px; top: 70px;
    display: flex; align-items: center; gap: 22px;
  }
  .brand-mark__square {
    width: 120px; height: 120px; background: var(--brand-blue);
  }
  .brand-mark__name {
    font-weight: 800; font-size: 40px; line-height: 1.05;
    color: var(--ink); letter-spacing: 0.5px;
  }
  .company-name {
    position: absolute; left: 50px; top: 222px;
    font-weight: 800; font-size: 34px; letter-spacing: 0.5px;
    white-space: nowrap;
  }
  .company-tagline {
    position: absolute; left: 52px; top: 268px;
    font-family: "Questrial", sans-serif;
    font-size: 34px; color: var(--brand-blue); letter-spacing: 1px;
    white-space: nowrap;
  }
  .divider {
    position: absolute; left: 0; top: 338px;
    width: 615px; height: 2px; background: var(--brand-blue-deep);
  }
  .address {
    position: absolute; left: 50px; top: 372px;
    font-size: 25px; white-space: nowrap;
  }
  .contacts {
    position: absolute; left: 50px; top: 426px;
    display: flex; gap: 18px; align-items: flex-start;
  }
  .contact-list { list-style: none; }
  .contact-list li {
    display: flex; align-items: center; gap: 9px;
    font-size: 25px; line-height: 36px; white-space: nowrap;
  }
  .contact-list--web li { font-size: 19px; line-height: 36px; }
  .contact-list svg { width: 18px; height: 18px; fill: var(--brand-blue); flex: none; }
  .portrait-frame {
    position: absolute; left: 640px; top: 35px;
    width: 380px; height: 490px;
    border: 4px solid var(--brand-blue);
    background: linear-gradient(160deg, var(--photo-top), var(--photo-bottom));
  }
  .name-band {
    position: absolute; left: 640px; top: 415px;
    width: 380px; height: 110px;
    background: var(--brand-blue);
    color: var(--paper);
    padding: 22px 0 0 50px;
  }
  .name-band__name { font-weight: 600; font-size: 36px; line-height: 1; }
  .name-band__title { font-size: 24px; margin-top: 4px; }
</style>
</head>
<body>
  <main class="card">
    <div class="brand-mark">
      <div class="brand-mark__square"></div>
      <div class="brand-mark__name">Q &amp; Q<br>Fabrications</div>
    </div>
    <div class="company-name">Q &amp; Q FABRICATIONS, INC.</div>
    <div class="company-tagline">Mechanical Contractor</div>
    <div class="divider"></div>
    <div class="address">4120 Larkin Road Fairview, WI 53999-0142</div>
    <div class="contacts">
      <ul class="contact-list contact-list--phones">
        <li><svg viewBox="0 0 20 20"><path d="M5 2l3 4-2 2c1 3 3 5 6 6l2-2 4 3-2 3C8 18 2 12 2 4z"/></svg>555-014-2210</li>
        <li><svg viewBox="0 0 20 20"><path d="M1 7c5-5 13-5 18 0l-3 2-2-2H6L4 9zM5 10h10l3 7H2z"/></svg>555-014-2211</li>
        <li><svg viewBox="0 0 20 20"><path d="M5 2h8v5H5zM2 8h16v8h-3v2H5v-2H2zM7 13v3h6v-3z"/></svg>555-014-2212</li>
      </ul>
      <ul class="contact-list contact-list--web">
        <li><svg viewBox="0 0 20 20"><path d="M1 4h18v12H1zM2 5l8 6 8-6v1l-8 6-8-6z"/></svg>dmarsh@qqfabrications-example.com</li>
        <li><svg viewBox="0 0 20 20"><circle cx="10" cy="10" r="8" fill="none" stroke="#3a70c0" stroke-width="2"/><path d="M2 10h16M10 2v16" stroke="#3a70c0" stroke-width="1.5"/></svg>www.qqfabrications-example.com</li>
      </ul>
    </div>
    <div class="portrait-frame" role="img" aria-label="Portrait photograph of the staff member in a dark suit"></div>
    <div class="name-band">
      <div class="name-band__name">Dale Marsh</div>
      <div class="name-band__title">Head of IT Services</div>
    </div>
  </main>
</body>
</html>
```